Valduro.com needs a Mobile FIRST Site

Valduro.com is an insurance broker based in Panama City, Panama that plans to sell car and motorcycle insurance online.

We need to design a total of 5 pages (two of those are A/B test pages). The site will be responsive and will be programmed in React. We will be using Brisk Widget´s library to code Valduro.com. Keep in mind that we are using Brisk Widget to program the site´s functions, not to create the "look and feel" of the site, that is obviously your job. You can learn more about Brisk Widget here... https://brisk-widget.example/

We have created wireframes for the app. Please follow and keep in mind the instructions in the wireframes. You can change things here and there as long as the core functions and goals stay intact. We have uploaded the wireframes along with the company logo and color.

We are planning to A/B test the site´s home page so we need to design two homepages. You can find homepage A and B in the wireframes provided.

We speak Spanish in Panama but you can design the site in English. We can change the text once we receive the designs.

Target Market(s)

25-45 year olds who own a car or motorcylcle and own a credit card.

Industry/Entity Type

Insurance

Font styles to use
Sans Serif

Requirements
Must have
• Follow the wireframes provided and the logo colors.
Nice to have
• Please look at the Image I´ve uploaded from DeskHaven, use it as reference to create HomePage A.

```html
<!DOCTYPE html>
<html lang="es">
<head>
<meta charset="utf-8">
<title>Valduro.com – Mobile screens</title>
<link rel="stylesheet" href="https://fonts.googleapis.com/css2?family=Roboto:wght@300;400;500;700&display=swap">
<style>
  :root {
    --purple: #5b2a86;
    --purple-deep: #4a1f73;
    --blue: #4b62c6;
    --grad: linear-gradient(90deg, #4b62c6 0%, #6a2d90 100%);
    --grad-head: linear-gradient(100deg, #4d5ec4 0%, #6b2f92 100%);
    --ink: #3a2a55;
    --muted: #8a8a96;
    --line: #b9a7cf;
    --bg: #ffffff;
    --screen-border: #e2e0e8;
  }
  * { box-sizing: border-box; margin: 0; padding: 0; }
  html, body { width: 1192px; height: 1200px; overflow: hidden; background: var(--bg); }
  body { position: relative; font-family: "Roboto", Arial, sans-serif; color: var(--ink); }

  .screen {
    position: absolute; background: #fff; overflow: hidden;
    border: 1px solid var(--screen-border);
    box-shadow: 0 4px 14px rgba(40, 20, 70, .12);
  }
  .screen--welcome { left: 467px; top: 114px; width: 228px; height: 395px; }
  .screen--form    { left: 77px;  top: 689px; width: 208px; height: 358px; }
  .screen--cars    { left: 370px; top: 694px; width: 199px; height: 345px; }
  .screen--motos   { left: 617px; top: 686px; width: 208px; height: 362px; }
  .screen--pay     { left: 887px; top: 678px; width: 215px; height: 371px; }

  /* Welcome */
  .brand {
    position: absolute; top: 84px; left: 0; right: 0; text-align: center;
    font-weight: 700; font-size: 30px; color: var(--purple); letter-spacing: -.5px;
  }
  .btn-login {
    position: absolute; top: 233px; left: 42px; width: 145px; height: 34px;
    border-radius: 17px; background: var(--grad); color: #fff;
    font-size: 14px; display: flex; align-items: center; justify-content: center; letter-spacing: .5px;
  }
  .signup-hint { position: absolute; top: 282px; left: 0; right: 0; text-align: center; font-size: 7px; color: var(--muted); font-weight: 300; }
  .btn-register {
    position: absolute; top: 294px; left: 42px; width: 145px; height: 34px;
    border-radius: 17px; border: 1.5px solid var(--purple); color: var(--purple-deep);
    font-size: 14px; display: flex; align-items: center; justify-content: center; letter-spacing: .5px;
  }

  /* Shared header */
  .steps {
    position: relative; height: 48px; background: var(--grad-head); color: #fff;
  }
  .steps svg { position: absolute; inset: 0; }
  .steps ul {
    position: absolute; bottom: 3px; left: 0; right: 0; list-style: none;
    display: flex; justify-content: space-between; padding: 0 14px 0 16px; font-size: 11px; font-weight: 300;
  }
  .steps li.is-active { border-bottom: 2px solid #fff; padding-bottom: 1px; }

  .vehicle-toggle {
    display: flex; margin: 8px auto 0; width: 168px; height: 22px;
    border: 1px solid var(--purple); border-radius: 3px; overflow: hidden; font-size: 10px;
  }
  .vehicle-toggle span {
    flex: 1; display: flex; align-items: center; justify-content: center; gap: 4px; color: var(--purple);
  }
  .vehicle-toggle span.is-active { background: var(--purple); color: #fff; }
  .v-icon { width: 22px; height: 8px; border-radius: 4px 6px 2px 2px; background: currentColor; opacity: .85; }
  .v-icon--moto { width: 16px; height: 9px; border-radius: 50% 50% 2px 2px; }

  /* Form screen */
  .plan-card { margin: 18px 13px 0; border: 1px solid var(--line); border-top: none; height: 260px; }
  .plan-card__head {
    height: 28px; background: var(--purple); color: #fff; display: flex; align-items: center;
    padding: 0 8px; font-size: 7px; gap: 30px;
  }
  .plan-card__head .arrow { font-size: 11px; }
  .plan-card__head .plan { margin-left: auto; line-height: 1.15; }
  .plan-card__body { padding: 8px 7px; font-size: 6px; color: var(--muted); }
  .plan-card__body h3 { font-size: 10px; font-weight: 400; color: var(--ink); }
  .field-value { font-size: 7px; color: var(--ink); border-bottom: 1px solid var(--line); width: 125px; padding: 6px 0 2px; margin-bottom: 6px; }
  .label { display: block; margin-top: 3px; }
  .radios { display: flex; gap: 30px; margin: 16px 0 0 5px; align-items: center; }
  .radios i { display: inline-block; width: 7px; height: 7px; border-radius: 50%; background: var(--purple); margin-right: 8px; vertical-align: -1px; }
  .id-row { display: flex; gap: 20px; margin-top: 16px; }
  .box { border: 1px solid var(--line); height: 13px; font-size: 7px; color: var(--ink); display: flex; align-items: center; justify-content: center; }
  .date-row { display: flex; gap: 3px; align-items: center; margin-top: 3px; font-size: 7px; color: var(--ink); }

  /* Product cards */
  .products { display: flex; gap: 3px; margin: 12px 0 0 15px; position: relative; }
  .products--wide { margin-left: 17px; }
  .product {
    width: 82px; border: 1px solid var(--line); padding: 4px 4px 6px; font-size: 7px;
  }
  .products--wide .product { width: 85px; }
  .product__photo { height: 42px; border-radius: 4px; }
  .photo-red { background: radial-gradient(ellipse at 50% 60%, #d8262e 0%, #e8a0a3 55%, #fff 80%); }
  .photo-orange { background: radial-gradient(ellipse at 50% 60%, #e98a2a 0%, #f2c796 55%, #fff 80%); }
  .photo-dark { background: radial-gradient(ellipse at 50% 55%, #3a3a3a 0%, #a5a5a5 55%, #fff 82%); }
  .photo-yellow { background: radial-gradient(ellipse at 50% 55%, #e2c520 0%, #555 45%, #ddd 68%, #fff 85%); }
  .product__price { font-size: 10px; color: var(--ink); margin: 4px 0 6px; font-weight: 300; }
  .product hr { border: none; border-top: 1px solid #bcc6ea; margin: 0 6px 9px 3px; }
  .metric { color: var(--ink); font-size: 7px; margin-left: 3px; }
  .bar { height: 9px; border: 1px solid var(--line); margin: 2px 0 10px 3px; width: 68px; position: relative; }
  .bar::before { content: ""; position: absolute; left: 0; top: 0; bottom: 0; width: var(--fill, 60%); background: var(--grad); }
  .product h4 { font-size: 10px; font-weight: 400; color: var(--ink); margin: 0 0 3px 3px; }
  .product p { font-size: 4px; line-height: 1.35; color: #666; margin: 0 2px 3px 3px; }
  .btn-buy {
    display: block; margin: 0 auto; width: 68px; height: 12px; border-radius: 3px;
    background: var(--grad); color: #fff; font-size: 8px; font-weight: 500; text-align: center; line-height: 12px;
  }
  .more-dot { position: absolute; right: -12px; top: 122px; width: 5px; height: 5px; border-radius: 50%; border: 1.5px solid var(--blue); }

  /* Pay screen */
  .claim { text-align: center; color: var(--purple-deep); }
  .claim h2 { font-size: 12px; font-weight: 500; margin-top: 20px; letter-spacing: .3px; }
  .claim p { font-size: 11px; line-height: 1.3; margin: 10px 16px 0; text-align: left; font-weight: 500; }
  .policy-card { margin: 14px 18px 0; border: 1px solid var(--line); height: 202px; }
  .policy-card__bar { height: 20px; background: var(--grad-head); }
  .policy-card h5 { font-size: 8px; font-weight: 400; color: var(--ink); text-align: center; margin-top: 8px; }
  .policy-doc { width: 42px; height: 36px; margin: 8px auto 0; background: linear-gradient(135deg, #9fb4e8, #4d6fd0); border-radius: 3px; }
  .actions { list-style: none; margin: 16px 0 0 38px; font-size: 8px; color: var(--ink); }
  .actions li { display: flex; align-items: center; gap: 6px; margin-bottom: 9px; }
  .actions svg { width: 18px; height: 16px; }
</style>
</head>
<body>

  <!-- Welcome -->
  <section class="screen screen--welcome">
    <div class="brand">Valduro.com</div>
    <div class="btn-login">LOGIN</div>
    <div class="signup-hint">Don't have an account?</div>
    <div class="btn-register">REGISTER</div>
  </section>

  <!-- Driver data -->
  <section class="screen screen--form">
    <header class="steps">
      <svg viewBox="0 0 208 48" preserveAspectRatio="none"><path d="M150 0 C135 20 175 38 208 26" fill="none" stroke="#8a5fb5" stroke-width="1"/><path d="M185 0 C178 12 195 18 208 14" fill="none" stroke="#8a5fb5" stroke-width="1"/></svg>
      <ul><li>Elige</li><li>Datos</li><li>Paga</li></ul>
    </header>
    <div class="vehicle-toggle">
      <span class="is-active"><i class="v-icon"></i>Carros</span>
      <span><i class="v-icon v-icon--moto"></i>Motos</span>
    </div>
    <div class="plan-card">
      <div class="plan-card__head">
        <span class="arrow">←</span>
        <i class="v-icon" style="background:#fff"></i>
        <span class="plan">Corvalia Plan B<br>$150</span>
      </div>
      <div class="plan-card__body">
        <h3>Datos del conductor</h3>
        <span class="label">Nombre Completo</span>
        <div class="field-value">Tomás Rivera</div>
        <span class="label">E-mail</span>
        <div class="field-value">trivera@mailbox.example</div>
        <span class="label">No. de Identificación</span>
        <div class="radios"><span><i></i>Cedula</span><span><i></i>Pasaporte</span></div>
        <div class="id-row">
          <div class="box" style="width:22px">00</div>
          <div class="box" style="width:12px;margin-left:-21px">▾</div>
          <div class="box" style="width:28px"></div>
          <div class="box" style="width:28px"></div>
        </div>
        <span class="label" style="margin-top:14px">Fecha de Nacimiento</span>
        <div class="date-row"><div class="box" style="width:20px">DD</div>/<div class="box" style="width:20px">MM</div>/<div class="box" style="width:20px">AA</div></div>
      </div>
    </div>
  </section>

  <!-- Cars -->
  <section class="screen screen--cars">
    <header class="steps">
      <svg viewBox="0 0 199 48" preserveAspectRatio="none"><path d="M140 0 C128 20 165 38 199 26" fill="none" stroke="#8a5fb5" stroke-width="1"/><path d="M176 0 C170 12 186 18 199 14" fill="none" stroke="#8a5fb5" stroke-width="1"/></svg>
      <ul><li>Elige</li><li>Datos</li><li>Paga</li></ul>
    </header>
    <div class="vehicle-toggle">
      <span class="is-active"><i class="v-icon"></i>Carros</span>
      <span><i class="v-icon v-icon--moto"></i>Motos</span>
    </div>
    <div class="products">
      <article class="product">
        <div class="product__photo photo-red" role="img" aria-label="Red hatchback car photo"></div>
        <div class="product__price">$150.00</div><hr>
        <div class="metric">xxx</div><div class="bar" style="--fill:60%"></div>
        <div class="metric">xxx</div><div class="bar" style="--fill:75%"></div>
        <div class="metric">xxx</div><div class="bar" style="--fill:85%"></div>
        <h4>Beneficios</h4>
        <p>Full coverage, roadside help and third party liability included.</p>
        <span class="btn-buy">COMPRAR</span>
      </article>
      <article class="product">
        <div class="product__photo photo-orange" role="img" aria-label="Orange compact SUV photo"></div>
        <div class="product__price">$170.00</div><hr>
        <div class="metric">xxx</div><div class="bar" style="--fill:55%"></div>
        <div class="metric">xxx</div><div class="bar" style="--fill:70%"></div>
        <div class="metric">xxx</div><div class="bar" style="--fill:85%"></div>
        <h4>Beneficios</h4>
        <p>Full coverage, roadside help and third party liability included.</p>
        <span class="btn-buy">COMPRAR</span>
      </article>
      <i class="more-dot"></i>
    </div>
  </section>

  <!-- Motorcycles -->
  <section class="screen screen--motos">
    <header class="steps">
      <svg viewBox="0 0 208 48" preserveAspectRatio="none"><path d="M150 0 C135 20 175 38 208 26" fill="none" stroke="#8a5fb5" stroke-width="1"/><path d="M185 0 C178 12 195 18 208 14" fill="none" stroke="#8a5fb5" stroke-width="1"/></svg>
      <ul><li>Elige</li><li>Datos</li><li>Paga</li></ul>
    </header>
    <div class="vehicle-toggle">
      <span><i class="v-icon"></i>Carros</span>
      <span class="is-active"><i class="v-icon v-icon--moto"></i>Motos</span>
    </div>
    <div class="products products--wide">
      <article class="product">
        <div class="product__photo photo-dark" role="img" aria-label="Black cruiser motorcycle photo"></div>
        <div class="product__price">$150.00</div><hr>
        <div class="metric">xxx</div><div class="bar" style="--fill:55%"></div>
        <div class="metric">xxx</div><div class="bar" style="--fill:80%"></div>
        <div class="metric">xxx</div><div class="bar" style="--fill:80%"></div>
        <h4>Beneficios</h4>
        <p>Full coverage, roadside help and third party liability included.</p>
        <span class="btn-buy">COMPRAR</span>
      </article>
      <article class="product">
        <div class="product__photo photo-yellow" role="img" aria-label="Yellow sport motorcycle photo"></div>
        <div class="product__price">$150.00</div><hr>
        <div class="metric">xxx</div><div class="bar" style="--fill:55%"></div>
        <div class="metric">xxx</div><div class="bar" style="--fill:80%"></div>
        <div class="metric">xxx</div><div class="bar" style="--fill:80%"></div>
        <h4>Beneficios</h4>
        <p>Full coverage, roadside help and third party liability included.</p>
        <span class="btn-buy">COMPRAR</span>
      </article>
      <i class="more-dot"></i>
    </div>
  </section>

  <!-- Payment / policy -->
  <section class="screen screen--pay">
    <header class="steps">
      <svg viewBox="0 0 215 48" preserveAspectRatio="none"><path d="M155 0 C140 20 180 38 215 26" fill="none" stroke="#8a5fb5" stroke-width="1"/><path d="M190 0 C184 12 200 18 215 14" fill="none" stroke="#8a5fb5" stroke-width="1"/></svg>
      <ul><li>Elige</li><li>Datos</li><li class="is-active">Paga</li></ul>
    </header>
    <div class="claim">
      <h2>CLAIM AQUI</h2>
      <p>Lorem ipsum dolor sit amet, consectetuer adipiscing elit,</p>
    </div>
    <div class="policy-card">
      <div class="policy-card__bar"></div>
      <h5>Tu polza de seguro..</h5>
      <div class="policy-doc" role="img" aria-label="Insurance policy document illustration"></div>
      <ul class="actions">
        <li><svg viewBox="0 0 18 16"><rect x="1" y="2" width="12" height="13" fill="none" stroke="#4b62c6"/><path d="M6 11 L15 2 L17 4 L8 13 L5 14 Z" fill="none" stroke="#4b62c6"/></svg>Cambiar datos</li>
        <li><svg viewBox="0 0 18 16"><rect x="1" y="3" width="16" height="11" fill="none" stroke="#4b62c6"/><path d="M1 3 L9 10 L17 3 M1 14 L7 8 M17 14 L11 8" fill="none" stroke="#4b62c6"/></svg>Enviar a otro e-mail</li>
        <li><svg viewBox="0 0 18 16"><path d="M9 1 V10 M5 6 L9 10 L13 6" fill="none" stroke="#4b62c6" stroke-width="1.6"/><path d="M2 10 V15 H16 V10" fill="none" stroke="#4b62c6" stroke-width="1.6"/></svg>Descargar</li>
      </ul>
    </div>
  </section>

</body>
</html>
```